Flyer-Design
Sehr flexibel bei Änderungswünschen. Herzlichen Dank. Würde jederzeit wieder mit Ursula zusammenarbeiten.
Zielgruppe
Wir sind eine eine Praxis und unsere Zielgruppe sind Kunden. Es sollte einen Faltflyer geben, welcher Doppelseitig bedruckt wird.
Aufgabenstellung
Ich habe genaue Vorstellungen, wie dieser Flyer aussehen soll. Jedoch bin ich auch auf neue Ideen gespannt :). Wunschvorstellung wäre ein Falzflyer (siehe Bild Musterfyler). Des weiteren habe ich ein Word gemacht, mit dem gesamten Inhalt des Textes und wie der Flyer am Besten aufgebaut werden sollte. (siehe Flyer Tierversicherung).
Die beiden letzten Abschnitte (Tipp an unsere Kunden, Fazit) sollten ein wenig auffallen. Müssen auch nicht am Schluss sein.
Des weiteren wäre ich dankbar, wenn das CI/CD der Unternehmung berücksichtig wird. Bitte werfen Sie einen Blick auf die Webseite www.felbor-tieraerzte.ch. Ein Logo ist ebenfalls im Anhang. Bei Fragen bitte melden.
Ich freue mich auf Vorschläge.

```html
<!DOCTYPE html>
<html lang="de">
<head>
<meta charset="utf-8">
<title>Felbor Tierärzte – Tierversicherungen Flyer</title>
<link href="https://fonts.googleapis.com/css2?family=Fira+Sans:ital,wght@0,300;0,400;0,500;0,600;1,300;1,400&display=swap" rel="stylesheet">
<style>
  :root {
    --brand-red: #cc1a45;
    --ink: #1c1c1c;
    --fur-light: #f3f1f1;
    --fur-mid: #e7e3e3;
    --panel-white: #fdfdfd;
    --logo-grey: #8a8a8a;
  }
  * { margin: 0; padding: 0; box-sizing: border-box; }
  html, body { width: 1200px; height: 848px; overflow: hidden; }
  body { font-family: "Fira Sans", sans-serif; color: var(--ink); background: var(--fur-light); }
  .flyer { position: relative; width: 1200px; height: 848px; overflow: hidden; }
  .fur-texture {
    position: absolute; inset: 0;
    background: linear-gradient(135deg, var(--fur-light) 0%, var(--fur-mid) 45%, var(--fur-light) 70%, var(--fur-mid) 100%);
  }
  .middle-panel {
    position: absolute; left: 391px; top: 0; width: 357px; height: 833px;
    background: linear-gradient(90deg, rgba(250,250,250,.85) 0 45px, var(--panel-white) 45px 310px, rgba(250,250,250,.85) 310px);
  }
  .bottom-band { position: absolute; left: 0; bottom: 0; width: 1200px; height: 15px; background: var(--brand-red); }

  .intro {
    position: absolute; left: 37px; top: 115px; width: 330px;
    font-size: 16.3px; line-height: 20.5px; font-weight: 400;
  }
  .intro p { margin-bottom: 20.5px; }
  .intro .intro-highlight { color: var(--brand-red); }

  .hours-title {
    position: absolute; left: 391px; width: 357px; top: 233px; text-align: center;
    color: var(--brand-red); font-weight: 600; font-size: 19.5px; letter-spacing: .4px;
  }
  .hours-table { position: absolute; left: 457px; top: 300px; font-size: 17px; font-weight: 500; line-height: 22.5px; }
  .hours-row { display: flex; }
  .hours-day { width: 120px; }
  .hours-note {
    position: absolute; left: 391px; width: 357px; top: 406px; text-align: center;
    font-style: italic; font-size: 16.3px; line-height: 20.5px;
  }
  .contact-rule { position: absolute; left: 504px; top: 669px; width: 175px; height: 1.5px; background: var(--brand-red); }
  .contact {
    position: absolute; left: 391px; width: 357px; top: 698px; text-align: center;
    font-size: 15.3px; line-height: 20px;
  }
  .contact .contact-name { font-weight: 600; }
  .contact b { font-weight: 600; }

  .cover-frame { position: absolute; left: 0; top: 0; }
  .brand-name {
    position: absolute; left: 880px; top: 216px; width: 240px; text-align: center;
    font-weight: 400; font-size: 27px; letter-spacing: 2px; color: var(--logo-grey); text-transform: uppercase;
  }
  .cover-title {
    position: absolute; left: 828px; width: 343px; top: 334px; text-align: center;
    color: var(--brand-red); font-weight: 600; font-size: 23.5px; line-height: 29px;
  }
  .cover-question {
    position: absolute; left: 828px; width: 343px; top: 422px; text-align: center;
    font-weight: 400; font-size: 22px; letter-spacing: .5px;
  }
</style>
</head>
<body>
<div class="flyer">
  <div class="fur-texture" role="img" aria-label="Heller, weicher Tierfell-Hintergrund"></div>
  <div class="middle-panel"></div>

  <section class="intro">
    <p>Haustiere sind für viele von uns von grosser Bedeutung und sensible Weggefährten, mit denen sich lachen, reden und auch einmal weinen lässt. Neben den vielen Vorzügen, die ein eigenes Haustier mit sich bringen, können diese auch krank werden oder einen Unfall haben.</p>
    <p>Wenn eine Behandlung das geliebte Haus­tier retten kann, jedoch hohe Kosten für Medikamente, Behandlungen, Operationen oder Klinikaufenthalte auslöst, dann entste­hen bei vielen Personen ernsthafte Sorgen und Belastungen, denen allerdings vorge­beugt werden kann.</p>
    <p>Mit einem Abschluss einer Tierversicherung gegen Unfall und Krankheit können ver­schiedene Vorkehrungen getroffen werden, um hohe Kosten im Ernstfall zu reduzieren.</p>
    <p>Daher ist es wichtig, dass man sich vor­gängig über die Möglichkeiten einer Tier­versicherung gegen Unfall und Krankheit informiert, um bestmöglich vorbereitet zu sein, sollte es dem treuen Begleiter einmal schlecht gehen.</p>
    <p class="intro-highlight">In diesem Flyer finden Sie alles von A-Z, was sie über Tierversicherungen gegen Unfall und Krankheit wissen müssen.</p>
  </section>

  <h2 class="hours-title">PRAXISÖFFNUNGSZEITEN</h2>
  <div class="hours-table">
    <div class="hours-row"><span class="hours-day">Mo bis Fr</span><span>8.00 – 12.00 und<br>13.30 - 18.00 Uhr</span></div>
    <div class="hours-row"><span class="hours-day">Sa</span><span>8.00 – 12.00 Uhr</span></div>
  </div>
  <p class="hours-note">Dringende Notfälle auch ausserhalb<br>der Kliniköffnungszeiten.</p>

  <div class="contact-rule"></div>
  <address class="contact" style="font-style:normal">
    <div class="contact-name">FELBOR TIERÄRZTE</div>
    <div>Kleintier AG / Grosstier AG</div>
    <div>Lindenweg 7 &nbsp;I&nbsp; 6430 Schwyz</div>
    <div><b>T</b> 041 555 01 20 &nbsp;I&nbsp; <b>F</b> 041 555 01 22</div>
    <div>info@felbor-tieraerzte.ch</div>
  </address>

  <svg class="cover-frame" width="1200" height="848" viewBox="0 0 1200 848" aria-hidden="true">
    <path fill="#ffffff" stroke="#cc1a45" stroke-width="3"
      d="M840 142 Q856.25 133 872.5 142 T905 142 T937.5 142 T970 142 T1002.5 142 T1035 142 T1067.5 142 T1100 142 T1132.5 142 T1165 142
         Q1174 158.8 1165 175.7 T1165 209.4 T1165 243.1 T1165 276.8 T1165 310.5 T1165 344.2 T1165 377.9 T1165 411.6 T1165 445.3 T1165 479 T1165 512.7 T1165 546.4 T1165 580
         Q1148.75 589 1132.5 580 T1100 580 T1067.5 580 T1035 580 T1002.5 580 T970 580 T937.5 580 T905 580 T872.5 580 T840 580
         Q831 563.2 840 546.4 T840 512.7 T840 479 T840 445.3 T840 411.6 T840 377.9 T840 344.2 T840 310.5 T840 276.8 T840 243.1 T840 209.4 T840 175.7 T840 142 Z"/>
  </svg>
  <div class="brand-name">Felbor Tierärzte</div>
  <h1 class="cover-title">Tierversicherungen gegen<br>Unfall und Krankheit</h1>
  <p class="cover-question">FLUCH ODER SEGEN?</p>

  <div class="bottom-band"></div>
</div>
</body>
</html>
```